Flyer for Beacon Ledger & Returns, a local tax practice

Flyer for my business to be distributed locally in the Western Suburb of Melbourne (Size: DL, Fold: Flat, Backside: Blank) This will include below information (Font, color and capitalization of the text is for the designer's creativity):
Beacon Ledger & Returns Your Local Tax Accountant
ABN: 71 284 519 036
Address: 9 Mirra Close, Tarwin Heights
dovpelk@blrau.com.au
Call Florin on 0417 865 209 to book your appointment
Services we offer:
Individual & Company Tax Returns
Company & Trust formation
Business Advisory
Bookkeeping
BAS & IAS
Payroll
TPAR
Please include the logo of the business attached which was designed by ArtHarbor few years ago.
Please include the QNE, WRD and Pulva logos somewhere in the bottom, preferable the same size and aligned (attached)

```html
<!DOCTYPE html>
<html lang="en">
<head>
<meta charset="utf-8">
<title>Beacon Ledger &amp; Returns – DL Flyer</title>
<link href="https://fonts.googleapis.com/css2?family=Poppins:wght@400;500;600;700;800&display=swap" rel="stylesheet">
<style>
  :root {
    --orange: #e8772e;
    --charcoal: #454547;
    --ink: #2e2e30;
    --paper: #ffffff;
    --backdrop: #c8c8c8;
    --rule: #d6d6d6;
    --badge-grey: #dcdcde;
    --photo-light: #c9ccd2;
    --photo-dark: #3c4048;
  }
  * { margin: 0; padding: 0; box-sizing: border-box; }
  html, body {
    width: 931px; height: 1200px; overflow: hidden;
    background: var(--backdrop);
    font-family: "Poppins", sans-serif;
  }
  .flyer {
    position: absolute; left: 215px; top: 53px;
    width: 476px; height: 1042px;
    background: var(--paper);
    transform: scale(1.05); transform-origin: top left;
    box-shadow: 3px 4px 8px rgba(0,0,0,.25);
    overflow: hidden;
  }
  .abs { position: absolute; }

  .brand {
    left: 0; width: 476px; top: 42px; height: 40px;
    display: flex; align-items: center; justify-content: center; gap: 10px;
  }
  .brand-mark { width: 34px; height: 34px; background: var(--charcoal); }
  .brand-name { font-size: 19px; font-weight: 600; color: var(--charcoal); }

  .headline {
    left: 0; width: 476px; top: 118px; text-align: center;
    font-weight: 800; font-size: 48px; line-height: 45px; color: var(--charcoal);
  }
  .headline .accent { color: var(--orange); }
  .headline .amp { font-weight: 400; }
  .tagline {
    left: 0; width: 476px; top: 256px; text-align: center;
    font-size: 18px; font-weight: 600; letter-spacing: .32em; color: var(--orange);
  }

  .photo {
    left: 0; top: 306px; width: 476px; height: 258px;
    background: linear-gradient(160deg, var(--photo-dark) 0%, #8a8f98 30%, var(--photo-light) 55%, #e6e8ec 75%, #7b8089 100%);
  }
  .photo-shade { left: 356px; top: 306px; width: 64px; height: 74px; background: rgba(40,40,44,.55); }
  .photo-band { left: 356px; top: 400px; width: 64px; height: 164px; background: var(--orange); opacity: .92; }

  .services-banner { left: 0; top: 564px; width: 420px; height: 53px; }
  .services-title {
    left: 41px; top: 572px; font-size: 28px; font-weight: 500; color: var(--paper);
  }
  .services-title strong { color: var(--orange); font-weight: 700; }

  .service-list { list-style: none; }
  .service-list li {
    display: flex; align-items: flex-start; gap: 5px;
    font-size: 17px; font-weight: 500; line-height: 20px; color: var(--ink);
    margin-bottom: 9px;
  }
  .service-list svg { flex: none; margin-top: 3px; }
  .services-left { left: 42px; top: 643px; width: 230px; }
  .services-right { left: 296px; top: 643px; }
  .column-rule { left: 276px; top: 640px; width: 1px; height: 120px; background: var(--rule); }

  .accreditation {
    top: 782px; width: 158px; height: 80px;
    display: flex; flex-direction: column; align-items: center; justify-content: center; gap: 4px;
  }
  .accreditation-row { display: flex; align-items: center; gap: 8px; }
  .accreditation-square { width: 30px; height: 30px; background: var(--charcoal); display: block; }
  .accreditation-square.is-orange { background: var(--orange); }
  .accreditation-circle { width: 34px; height: 34px; border-radius: 50%; background: var(--badge-grey); display: block; }
  .accreditation-name { font-size: 22px; font-weight: 600; color: var(--charcoal); }
  .accreditation-note { font-size: 8px; font-weight: 500; color: var(--charcoal); }
  .accreditation-rule { top: 782px; width: 1px; height: 80px; background: var(--rule); }

  .cta-shape { left: 0; top: 878px; width: 476px; height: 55px; }
  .cta-line {
    left: 0; width: 476px; top: 882px; text-align: center;
    font-size: 17px; font-weight: 600; color: var(--paper);
    display: flex; justify-content: center; align-items: center; gap: 8px;
  }
  .cta-line .phone { font-weight: 700; display: inline-flex; align-items: center; gap: 4px; }
  .cta-sub {
    left: 0; width: 476px; top: 906px; text-align: center;
    font-size: 13.5px; font-weight: 700; color: var(--ink);
  }

  .footer { left: 0; top: 933px; width: 476px; height: 109px; background: var(--charcoal); }
  .contact {
    left: 0; width: 476px; text-align: center;
    font-size: 15px; font-weight: 400; color: var(--paper);
    display: flex; justify-content: center; align-items: center; gap: 4px;
  }
  .contact-address { top: 944px; }
  .contact-email { top: 966px; }
  .abn {
    left: 164px; top: 995px; width: 143px; height: 20px;
    border: 1.5px solid var(--orange); border-radius: 10px;
    font-size: 9.5px; font-weight: 500; color: var(--paper);
    display: flex; align-items: center; justify-content: center; gap: 3px;
  }
  .abn strong { font-weight: 700; }
</style>
</head>
<body>
<main class="flyer">

  <div class="abs brand">
    <span class="brand-mark"></span>
    <span class="brand-name">Beacon Ledger &amp; Returns</span>
  </div>

  <h1 class="abs headline">
    <span class="accent">BEACON</span><br>
    LEDGER<br>
    <span class="amp">&amp;</span> RETURNS
  </h1>
  <p class="abs tagline">A LOCAL TAX PRACTICE</p>

  <div class="abs photo" role="img" aria-label="Photo of a hand holding a pen over financial reports and charts beside a calculator"></div>
  <div class="abs photo-shade"></div>
  <div class="abs photo-band"></div>

  <svg class="abs services-banner" viewBox="0 0 420 53" aria-hidden="true">
    <polygon points="0,0 420,0 367,53 0,53" fill="var(--charcoal)"/>
  </svg>
  <h2 class="abs services-title">SERVICES <strong>WE OFFER</strong></h2>

  <svg width="0" height="0" style="position:absolute">
    <symbol id="tick-box" viewBox="0 0 16 16">
      <rect x="1" y="3" width="11" height="11" rx="1.5" fill="none" stroke="var(--charcoal)" stroke-width="1.6"/>
      <path d="M4 8.5 L7 11.5 L14.5 2.5" fill="none" stroke="var(--orange)" stroke-width="2.4" stroke-linecap="round" stroke-linejoin="round"/>
    </symbol>
  </svg>

  <ul class="abs service-list services-left">
    <li><svg width="15" height="15"><use href="#tick-box"/></svg><span>Individual &amp; Company Tax Returns</span></li>
    <li><svg width="15" height="15"><use href="#tick-box"/></svg><span>Company &amp; Trust formation</span></li>
    <li><svg width="15" height="15"><use href="#tick-box"/></svg><span>Business Advisory</span></li>
  </ul>
  <div class="abs column-rule"></div>
  <ul class="abs service-list services-right">
    <li><svg width="15" height="15"><use href="#tick-box"/></svg><span>Bookkeeping</span></li>
    <li><svg width="15" height="15"><use href="#tick-box"/></svg><span>BAS &amp; IAS</span></li>
    <li><svg width="15" height="15"><use href="#tick-box"/></svg><span>Payroll</span></li>
    <li><svg width="15" height="15"><use href="#tick-box"/></svg><span>TPAR</span></li>
  </ul>

  <div class="abs accreditation" style="left:0;">
    <div class="accreditation-row">
      <span class="accreditation-square"></span>
      <span class="accreditation-name">QNE</span>
    </div>
  </div>
  <div class="abs accreditation-rule" style="left:158px;"></div>
  <div class="abs accreditation" style="left:159px;">
    <div class="accreditation-row">
      <span class="accreditation-square is-orange"></span>
      <span class="accreditation-name">Pulva</span>
    </div>
  </div>
  <div class="abs accreditation-rule" style="left:317px;"></div>
  <div class="abs accreditation" style="left:318px;">
    <div class="accreditation-row">
      <span class="accreditation-circle"></span>
      <span class="accreditation-name">WRD</span>
    </div>
    <p class="accreditation-note">Tax Agent 41870263</p>
  </div>

  <svg class="abs cta-shape" viewBox="0 0 476 55" aria-hidden="true">
    <polygon points="75,0 402,0 445,55 32,55" fill="var(--orange)"/>
  </svg>
  <p class="abs cta-line">
    <span>CALL FLORIN ON</span>
    <span class="phone">
      <svg width="14" height="14" viewBox="0 0 16 16" aria-hidden="true">
        <circle cx="8" cy="8" r="7.5" fill="var(--charcoal)"/>
        <path d="M5.2 4.2 L6.6 4 L7.4 6 L6.5 6.8 Q7.3 8.6 9.2 9.5 L10 8.6 L12 9.4 L11.8 10.8 Q9 11.5 6.6 9.4 Q4.5 7 5.2 4.2Z" fill="#fff"/>
      </svg>0417 865 209</span>
  </p>
  <p class="abs cta-sub">to book your appointment</p>

  <footer class="abs footer"></footer>
  <p class="abs contact contact-address">
    <svg width="10" height="13" viewBox="0 0 10 13" aria-hidden="true">
      <path d="M5 0.5 A4.5 4.5 0 0 1 9.5 5 C9.5 8 5 12.5 5 12.5 C5 12.5 0.5 8 0.5 5 A4.5 4.5 0 0 1 5 0.5Z" fill="var(--orange)"/>
      <circle cx="5" cy="5" r="1.7" fill="var(--charcoal)"/>
    </svg>
    9 Mirra Close, Tarwin Heights
  </p>
  <p class="abs contact contact-email">
    <svg width="12" height="9" viewBox="0 0 12 9" aria-hidden="true">
      <rect width="12" height="9" rx="1" fill="var(--orange)"/>
      <path d="M0.5 1 L6 5 L11.5 1" fill="none" stroke="var(--charcoal)" stroke-width="1"/>
    </svg>
    dovpelk@blrau.com.au
  </p>
  <p class="abs abn">ABN: <strong>71 284 519 036</strong></p>

</main>
</body>
</html>
```